Business Card Design For A Renovation Contractor Company

We need a business card for a new company based in Singapore, our company name is "KM Bravant". We are a renovation contractor that builds designs into reality. We build more of F&B restaurants, retail stores and commercial offices. We work very closely with designers. The final design should communicate to our client that we are a company that you can trust, that will plan and complete your project without giving you a headache. I like my client to remember my company as "KM". The beauty of SIMPLE is important.

Industry/Entity Type

Contractor

Requirements
Nice to have
• Black or Red base

```html
<!DOCTYPE html>
<html lang="en">
<head>
<meta charset="utf-8">
<title>KM Bravant – Business Card</title>
<link rel="stylesheet" href="https://fonts.googleapis.com/css2?family=Open+Sans:wght@300;400;600&display=swap">
<style>
  :root {
    --canvas-bg: #d9d6d2;
    --card-dark: #252525;
    --card-light: #ebebeb;
    --accent-red: #c8141c;
    --ink-dark: #2b2b2b;
    --ink-soft: #555555;
    --ink-light: #e8e8e8;
  }
  * { box-sizing: border-box; margin: 0; padding: 0; }
  html, body {
    width: 1200px; height: 900px; overflow: hidden;
    background: var(--canvas-bg);
    font-family: "Open Sans", Arial, sans-serif;
  }
  .canvas { position: relative; width: 1200px; height: 900px; }
  .card {
    position: absolute; width: 560px; height: 320px;
    box-shadow: 0 6px 18px rgba(0,0,0,.18);
    overflow: hidden;
  }
  /* Front side */
  .card--front { left: 110px; top: 90px; background: var(--card-dark); }
  .card--front .brand { position: absolute; left: 150px; top: 96px; }
  .card--front .front-rule {
    position: absolute; left: 0; right: 0; bottom: 32px;
    height: 3px; background: var(--accent-red);
  }
  /* Brand lockup */
  .brand { display: flex; flex-direction: column; align-items: flex-start; }
  .brand__row { display: flex; align-items: center; gap: 14px; }
  .brand__dot {
    width: 46px; height: 46px; border-radius: 50%;
    border: 3px solid var(--accent-red);
  }
  .brand__name {
    font-weight: 300; font-size: 40px; letter-spacing: .5px;
    color: var(--accent-red); line-height: 1;
  }
  .brand__tagline {
    margin-top: 8px; padding-top: 3px; margin-left: 60px;
    border-top: 1px solid currentColor;
    font-size: 13px; font-weight: 300; letter-spacing: .6px;
    white-space: nowrap;
  }
  .card--front .brand__tagline { color: var(--ink-light); }
  /* Back side */
  .card--back { left: 530px; top: 480px; background: var(--card-light); }
  .card--back .brand { position: absolute; left: 34px; top: 140px; }
  .card--back .brand__name { font-size: 32px; }
  .card--back .brand__dot { width: 38px; height: 38px; }
  .card--back .brand__tagline { font-size: 11px; margin-left: 52px; color: var(--ink-soft); }
  .contact { position: absolute; left: 330px; top: 50px; color: var(--ink-dark); }
  .contact__name { font-size: 17px; font-weight: 400; letter-spacing: .5px; }
  .contact__role { font-size: 11px; color: var(--ink-soft); margin-left: 16px; margin-bottom: 26px; }
  .contact__line { font-size: 11.5px; line-height: 1.55; display: flex; gap: 8px; }
  .contact__label { color: var(--accent-red); font-weight: 600; width: 10px; }
  .contact__address { font-size: 11.5px; line-height: 1.55; margin: 12px 0 0 18px; }
  .contact__web { font-size: 12px; font-weight: 600; margin: 6px 0 0 18px; }
  .contact__web span { color: var(--accent-red); }
</style>
</head>
<body>
<main class="canvas">
  <section class="card card--front" aria-label="Card front">
    <div class="brand">
      <div class="brand__row">
        <span class="brand__dot"></span>
        <span class="brand__name">KM Bravant</span>
      </div>
      <p class="brand__tagline">from design to finished space</p>
    </div>
    <div class="front-rule"></div>
  </section>

  <section class="card card--back" aria-label="Card back">
    <div class="brand">
      <div class="brand__row">
        <span class="brand__dot"></span>
        <span class="brand__name">KM Bravant</span>
      </div>
      <p class="brand__tagline">from design to finished space</p>
    </div>
    <div class="contact">
      <p class="contact__name">MARCUS LIM.</p>
      <p class="contact__role">Director</p>
      <p class="contact__line"><span class="contact__label">T</span><span>555.013.2468</span></p>
      <p class="contact__line"><span class="contact__label">E</span><span>marcus@kmbravant.com</span></p>
      <p class="contact__address">12 Tanjong Road,<br>#04-118 Tanjong Complex<br>Singapore 437001</p>
      <p class="contact__web">www.<span>kmbravant</span>.com</p>
    </div>
  </section>
</main>
</body>
</html>
```